Larkspan Communications ISP Flyer

Our company is Larkspan Communications. We need to create a flyer to market our Internet/Phone services to a retirement community. We will be offering 50x50 internet connection along with a single phone line for $49.99 (before taxes). We would like to emphasize that our services are over fiber optic cables.

Internet Service
- 50x50 megabit fiber internet connection
- up to 5 email addresses
- 10gb of online storage

Phone Service
- Local 956 Phone number
- Unlimited Local/Long distance
- Caller Id
- Web access to Voicemail

Target Market(s)

Residential Customers

Industry/Entity Type

Internet

Requirements
Must have
• Company Name - Larkspan Communications
Service detail

Contact info -

sales@larkspanco.example
956-483-2917

```html
<!DOCTYPE html>
<html lang="en">
<head>
<meta charset="utf-8">
<title>Larkspan Communications – Telephone and Internet Offer</title>
<link rel="stylesheet" href="https://fonts.googleapis.com/css2?family=Oswald:wght@500;700&family=Arimo:wght@400;700&display=swap">
<style>
  :root {
    --ink: #000000;
    --paper: #ffffff;
    --magenta: #ff1fa6;
    --green: #27d13a;
    --icon-green: #3bc43b;
    --display: "Oswald", "Arial Narrow", sans-serif;
    --body: "Arimo", Arial, sans-serif;
  }
  * { margin: 0; padding: 0; box-sizing: border-box; }
  html, body { width: 857px; height: 1200px; overflow: hidden; background: var(--ink); }
  .flyer {
    position: relative; width: 857px; height: 1200px;
    background: var(--ink); color: var(--paper); font-family: var(--body); overflow: hidden;
  }
  .headline { position: absolute; left: 22px; top: 18px; font-weight: 700; }
  .headline__lead { font-size: 40px; line-height: 1.1; }
  .headline__lead .accent { color: var(--magenta); font-size: 58px; font-family: var(--display); letter-spacing: 1px; }
  .headline__sub { font-size: 33px; margin-top: 10px; }
  .brain-visual {
    position: absolute; left: 275px; top: 205px; width: 385px; height: 300px;
    border-radius: 50% 50% 45% 45%;
    background: radial-gradient(ellipse at center, #e070ff 0%, #8e2fd6 35%, #3a0f5e 65%, var(--ink) 80%);
  }
  .equation {
    position: absolute; left: 0; right: 0; top: 505px; text-align: center;
    font-family: var(--display); font-weight: 700; font-size: 80px; letter-spacing: 1px; line-height: 1;
  }
  .offer-band {
    position: absolute; left: 0; top: 598px; width: 857px; height: 602px;
    border-top: 2px dashed var(--paper);
    background:
      radial-gradient(ellipse 70% 14% at 75% 42%, rgba(255,40,150,.55), transparent 70%),
      linear-gradient(160deg, #1b1b1b 0%, #050505 45%, #2a0a1c 70%, #000 100%);
  }
  .offer-title { position: absolute; left: 22px; top: 612px; font-family: var(--display); font-weight: 700; }
  .offer-title__burst { display: block; color: var(--magenta); font-size: 74px; line-height: 1; }
  .offer-title__line { display: block; font-size: 57px; line-height: 1.1; margin-top: 4px; }
  .icon-tile { position: absolute; background: var(--icon-green); border: 3px solid var(--paper); }
  .icon-tile--phone { left: 26px; top: 825px; width: 130px; height: 125px; }
  .icon-tile--home { left: 660px; top: 850px; width: 125px; height: 112px; }
  .icon-tile svg { width: 100%; height: 100%; display: block; }
  .fibre-tag {
    position: absolute; left: 22px; top: 965px; font-family: var(--display); font-weight: 700;
    line-height: 0.95; transform: rotate(-4deg);
  }
  .fibre-tag__word { display: block; font-size: 42px; color: var(--paper); }
  .fibre-tag__word--hot { color: var(--magenta); }
  .fibre-tag__small { display: block; font-size: 18px; letter-spacing: 1px; }
  .services { position: absolute; left: 256px; top: 800px; width: 390px; font-size: 18px; line-height: 26px; }
  .services__heading { color: var(--green); font-weight: 700; font-size: 22px; line-height: 28px; }
  .services__list { list-style: none; }
  .price { position: absolute; right: 30px; top: 990px; text-align: right; font-weight: 700; }
  .price__label { font-size: 20px; margin-right: 6px; }
  .price__amount { font-family: var(--display); color: var(--magenta); font-size: 78px; line-height: 1; }
  .contact__call {
    position: absolute; left: 0; right: 0; top: 1094px; text-align: center;
    color: var(--green); font-weight: 700; font-size: 26px; line-height: 30px;
  }
  .contact__company {
    position: absolute; left: 0; right: 0; top: 1126px; text-align: center;
    font-weight: 700; font-size: 18px; line-height: 22px;
  }
  .contact__details {
    position: absolute; left: 22px; right: 22px; top: 1152px;
    display: flex; justify-content: space-between; font-size: 32px; line-height: 38px;
  }
</style>
</head>
<body>
<main class="flyer">
  <header class="headline">
    <p class="headline__lead"><span class="accent">SOME</span> things are worked out for you...</p>
    <p class="headline__sub">...so you won't be needing one of these!</p>
  </header>

  <div class="brain-visual" role="img" aria-label="Glowing purple illustration of a human brain"></div>

  <p class="equation">50×50+10+5+956=49.99</p>

  <section class="offer-band" role="img" aria-label="Dark background with a glowing pink fibre optic light streak"></section>

  <h1 class="offer-title">
    <span class="offer-title__burst">AMAZING!</span>
    <span class="offer-title__line">Telephone line and Internet offer!</span>
  </h1>

  <div class="icon-tile icon-tile--phone">
    <svg viewBox="0 0 130 120" aria-hidden="true">
      <path d="M45 22c6-3 12 0 14 6l6 16c2 5 0 10-4 12l-6 4c4 10 12 19 22 24l5-6c3-4 8-5 12-3l15 8c5 3 7 9 4 14l-5 8c-4 5-11 7-18 4C58 98 36 74 30 46c-2-7 1-14 7-18z" fill="#ffffff"/>
    </svg>
  </div>

  <div class="fibre-tag">
    <span class="fibre-tag__word">FAST</span>
    <span class="fibre-tag__word fibre-tag__word--hot">FIBRE</span>
    <span class="fibre-tag__word fibre-tag__word--hot">OPTIC</span>
    <span class="fibre-tag__small">TECHNOLOGY</span>
  </div>

  <section class="services">
    <h2 class="services__heading">Internet Service</h2>
    <ul class="services__list">
      <li>50x50 megabit fiber internet connection</li>
      <li>10gb of online storage</li>
      <li>Up to 5 e mail addresses</li>
    </ul>
    <h2 class="services__heading">Phone Service</h2>
    <ul class="services__list">
      <li>Local 956 Phone number</li>
      <li>Unlimited Local/Long distance</li>
      <li>Caller Id</li>
      <li>Web access to Voicemail</li>
    </ul>
  </section>

  <div class="icon-tile icon-tile--home">
    <svg viewBox="0 0 112 100" aria-hidden="true">
      <path d="M18 52 L50 24 L82 52 M28 46 V84 H72 V46" fill="none" stroke="#ffffff" stroke-width="6" stroke-linejoin="round"/>
      <rect x="42" y="60" width="16" height="24" fill="#ffffff"/>
      <path d="M84 22a14 14 0 0 1 14 14 M84 12a24 24 0 0 1 24 24" fill="none" stroke="#ffffff" stroke-width="4" stroke-linecap="round"/>
    </svg>
  </div>

  <div class="price">
    <p class="price__label">ALL FOR JUST</p>
    <p class="price__amount">$49.99</p>
  </div>

  <footer class="contact">
    <p class="contact__call">Contact us now!</p>
    <p class="contact__company">Larkspan Communications</p>
    <p class="contact__details"><span>sales@larkspanco.example</span><span>956-483-2917</span></p>
  </footer>
</main>
</body>
</html>
```